Preschool Website

Looking to have a one page splash with a contact us form that uses some kind of verification to keep bots from filling out the form. We would like for it to be dynamic for both mobile and desktop. Would like to have it show up in search engines for preschool in are area. Would like to include a link to the website are current parents use for payment information.

Target Market(s)

Young Adults with Childrens

Industry/Entity Type

Preschool

Coding

Coded - Design and coding required

Number of Pages Required

1 page

Colors

Designer to choose colors to be used in the design.

Requirements
Must have
• Searchable in Vextra
• Contact us form
• Name
• Phone
• Email
• Message box
• Form must have code entered to submit to prevent junk emails
• Link to the website we use for parents to make payments
• our phone and address clickable on device to make call or map on phone
Should not have
• more then one page

```html
<!DOCTYPE html>
<html lang="en">
<head>
<meta charset="UTF-8">
<title>Preschool – Contact</title>
<link rel="stylesheet" href="https://fonts.googleapis.com/css2?family=Paytone+One&family=Poppins:wght@400;500;600&display=swap">
<style>
  :root {
    --green: #1fd38f;
    --magenta: #cc12a0;
    --magenta-soft: #e05ac4;
    --panel: #d5d5d5;
    --field: #ffffff;
    --text-light: #f4f4f4;
    --bg-top: #6b6b69;
    --bg-mid: #656462;
    --bg-bottom: #5b5047;
  }
  * { box-sizing: border-box; margin: 0; padding: 0; }
  html, body { width: 958px; height: 1200px; overflow: hidden; }
  body {
    position: relative;
    font-family: "Poppins", sans-serif;
    background: linear-gradient(180deg, var(--bg-top) 0%, var(--bg-mid) 55%, var(--bg-bottom) 100%);
    border-top: 5px solid var(--green);
    border-bottom: 5px solid var(--green);
  }
  .backdrop {
    position: absolute; inset: 0;
    background:
      radial-gradient(ellipse 160px 220px at 770px 760px, rgba(150,80,60,0.35), transparent 70%),
      radial-gradient(ellipse 260px 60px at 260px 1020px, rgba(150,130,90,0.25), transparent 70%);
  }
  .site-logo {
    position: absolute; left: 78px; top: 20px;
    font-family: "Poppins", sans-serif; font-weight: 600;
    font-size: 36px; color: var(--green); letter-spacing: 0.5px;
  }
  .contact-form {
    position: absolute; left: 79px; top: 84px;
    width: 282px; height: 459px;
    background: var(--panel);
    border: 1px solid #bdbdbd;
    border-radius: 8px;
    box-shadow: 0 2px 4px rgba(0,0,0,0.25);
  }
  .field {
    position: absolute; left: 20px; width: 240px; height: 32px;
    background: var(--field); border: none; border-radius: 9px;
    box-shadow: 0 2px 3px rgba(0,0,0,0.35);
    font-family: "Poppins", sans-serif; font-size: 13.5px;
    padding: 0 28px; color: var(--green);
  }
  .field::placeholder { color: var(--green); }
  .field--name { top: 27px; }
  .field--phone { top: 83px; }
  .field--email { top: 139px; }
  .field--code { top: 195px; }
  .field--message { top: 250px; height: 128px; padding-top: 6px; resize: none; }
  .btn {
    position: absolute;
    display: flex; align-items: center; justify-content: center;
    background: var(--magenta); color: #fff;
    font-family: "Poppins", sans-serif; border: none; text-decoration: none;
  }
  .btn--submit {
    left: 148px; top: 401px; width: 112px; height: 35px;
    border-radius: 9px; font-size: 14px; font-weight: 500;
  }
  .intro { position: absolute; left: 500px; top: 214px; width: 390px; }
  .intro__title, .section-title {
    font-family: "Paytone One", sans-serif; color: var(--green); font-weight: 400;
  }
  .intro__title { font-size: 30px; line-height: 40px; }
  .intro__text { margin-top: 4px; color: var(--text-light); font-size: 14.3px; line-height: 20px; }
  .section-title {
    position: absolute; font-size: 30px; line-height: 40px;
    width: 300px; text-align: center;
  }
  .section-title--touch { left: 89px; top: 661px; }
  .section-title--pay { left: 568px; top: 658px; }
  .art { position: absolute; }
  .art--phone {
    left: 174px; top: 730px; width: 132px; height: 137px; border-radius: 10px;
    background: linear-gradient(135deg, #e02fb0, #a10a82 70%, #e6d5c0);
  }
  .art--map {
    left: 174px; top: 967px; width: 128px; height: 109px; border-radius: 6px;
    background: linear-gradient(135deg, #d52aa8, #a40c86);
  }
  .art--payment {
    left: 638px; top: 822px; width: 156px; height: 156px; border-radius: 50%;
    background: radial-gradient(circle at 50% 50%, #d33aa8, #8e2a73 75%);
    opacity: 0.9;
  }
  .btn--wide {
    width: 222px; height: 47px; border-radius: 9px;
    font-size: 14.5px; font-weight: 600;
  }
  .btn--number { left: 128px; top: 891px; }
  .btn--address { left: 128px; top: 1091px; }
  .btn--payment { left: 606px; top: 998px; }
</style>
</head>
<body>
  <div class="backdrop" role="img" aria-label="Soft blurred photo of alphabet blocks, books and coloured pencils on a wooden table"></div>

  <div class="site-logo">LOGO</div>

  <form class="contact-form" action="#" method="post">
    <input class="field field--name" type="text" placeholder="Your Name" aria-label="Your Name">
    <input class="field field--phone" type="tel" placeholder="Your Phone" aria-label="Your Phone">
    <input class="field field--email" type="email" placeholder="Your Email" aria-label="Your Email">
    <input class="field field--code" type="text" placeholder="Enter Your Code" aria-label="Enter Your Code">
    <textarea class="field field--message" placeholder="Your Message" aria-label="Your Message"></textarea>
    <button class="btn btn--submit" type="submit">Contact Us</button>
  </form>

  <section class="intro">
    <h1 class="intro__title">Communication is key</h1>
    <p class="intro__text">Lorem ipsum dolor sit amet, consectetur adipisicing elit, sed do eiusmod tempor incididunt ut labore et dolore magna aliqua. Ut enim ad minim veniam, quis nostrud exercitation ullamco laboris nisi ut aliquip.</p>
  </section>

  <h2 class="section-title section-title--touch">Get In Touch</h2>
  <div class="art art--phone" role="img" aria-label="Illustration of a hand holding a smartphone with a contact card"></div>
  <a class="btn btn--wide btn--number" href="#">Get Our Number</a>
  <div class="art art--map" role="img" aria-label="Illustration of a folded map with a location pin"></div>
  <a class="btn btn--wide btn--address" href="#">Get Our Addres</a>

  <h2 class="section-title section-title--pay">Get to Payment</h2>
  <div class="art art--payment" role="img" aria-label="Illustration of a hand using a card payment terminal"></div>
  <a class="btn btn--wide btn--payment" href="#">Make Your Payment</a>
</body>
</html>
```